Prospective Client Introduction Brochure/Packet

We need a "Welcome Packet" for a Private Wealth Management Firm to give to prospective clients. It will need to be print ready as it is something we will hand to them or mail to them in a hard copy form. Might even need help designing a few extra pieces. Want a professional piece that share with people, who our firm is, what we do and how we help clients, We will need to provide pics and such but want to narrow down a "look"

Target Market(s)

Business owners and retiree's/ retired individuals

Industry/Entity Type

Financial Services

Font styles to use
Serif
Sans Serif

Colors
0054AA
0677BA
7BADD7
CADEEF
E8F1F8

Requirements
Must have
• Include the Alder Ridge logo as best as possible be easy to read
Nice to have
• Flow Chart's of the journey,
Should not have
• Cartoon like images

```html
<!DOCTYPE html>
<html lang="en">
<head>
<meta charset="utf-8">
<title>Alder Ridge Wealth Management – Welcome Packet</title>
<link href="https://fonts.googleapis.com/css2?family=Cormorant+Garamond:ital,wght@0,400;0,500;0,600;0,700;1,500&family=Mulish:wght@400;600;700&display=swap" rel="stylesheet">
<style>
:root{
  --backdrop:#dde8ef;
  --paper:#ffffff;
  --navy:#0b4266;
  --navy-deep:#08314f;
  --gold:#c9a227;
  --ink:#2a2a2a;
  --ink-soft:#3d3d3d;
  --label-blue:#2f97d6;
  --rule-light:#d6d6d6;
}
*{box-sizing:border-box;margin:0;padding:0}
html,body{width:976px;height:1200px;overflow:hidden}
body{background:var(--backdrop);position:relative;font-family:'Mulish',sans-serif;color:var(--ink)}
.page{position:absolute;width:392px;height:508px;background:var(--paper);overflow:hidden}
.page--cover{left:71px;top:65px}
.page--intro{left:513px;top:65px}
.page--compare{left:71px;top:623px}
.page--commitment{left:513px;top:623px}
.page__panel{position:absolute;left:10px;top:11px;right:10px;bottom:10px;
  background:linear-gradient(125deg,#e6e6e6 0%,#ececec 45%,#f4f4f4 55%,#e9e9e9 100%)}
.abs{position:absolute}

/* cover */
.brand-box{left:33px;top:0;width:145px;height:74px;background:var(--navy);color:#fff;
  display:flex;flex-direction:column;justify-content:center;align-items:center;
  font-family:'Cormorant Garamond',serif;font-weight:600;font-size:11.5px;line-height:15px;letter-spacing:1px;text-align:center}
.welcome-title{left:33px;top:166px;font-family:'Cormorant Garamond',serif;font-weight:700;font-size:40px;line-height:37px;color:var(--navy);letter-spacing:.5px}
.gold-rule{left:33px;top:263px;width:52px;height:2px;background:var(--gold)}
.cover-copy{left:33px;top:288px;width:215px;font-size:7.8px;line-height:11.6px;color:var(--ink)}
.cover-copy strong{color:var(--navy);font-weight:700}
.cover-copy p+p{margin-top:11.5px}
.band{left:0;width:392px}
.contact{left:29px;top:443px;color:#fff;font-size:7.8px;line-height:15px}
.contact__label{color:var(--label-blue)}
.contact__grid{display:flex}
.contact__col{padding-right:16px}
.contact__col+.contact__col{border-left:.8px solid var(--label-blue);padding-left:16px}

/* intro */
.intro-kicker{left:41px;top:34px;font-family:'Cormorant Garamond',serif;font-weight:700;font-size:22px;line-height:23px;color:#1b1b1b;letter-spacing:.5px}
.intro-kicker span{color:var(--gold);display:block}
.intro-sub{left:41px;top:88px;font-size:6.3px;letter-spacing:1.3px;color:#333;display:flex;align-items:center;gap:5px}
.intro-sub::after{content:"";width:60px;height:.6px;background:#888}
.intro-tagline{left:41px;top:111px;font-family:'Cormorant Garamond',serif;font-style:italic;font-weight:500;font-size:14.5px;color:var(--navy)}
.intro-copy{left:41px;top:143px;width:276px;font-size:6.5px;line-height:10.3px;color:var(--ink-soft)}
.intro-copy p+p{margin-top:10.3px}
.differ-title{left:41px;top:320px;font-family:'Cormorant Garamond',serif;font-size:11px;font-weight:500;color:#fff}
.differ-list{list-style:none;color:#fff;font-size:6.5px;line-height:10.3px}
.differ-list li{position:relative;padding-left:10px;margin-bottom:10.3px}
.differ-list li::before{content:"✓";position:absolute;left:0;color:var(--gold)}

/* compare */
.badge{left:27px;top:27px;width:52px;display:flex;flex-direction:column;align-items:center;gap:4px;font-weight:700;font-size:6.2px;line-height:7px;color:var(--navy);text-align:center;letter-spacing:.4px}
.badge__square{width:18px;height:18px;background:var(--gold)}
.compare-title{left:92px;top:28px;font-family:'Cormorant Garamond',serif;font-weight:600;font-size:13.8px;line-height:16.9px;color:var(--navy);letter-spacing:.3px}
.compare-title span{color:var(--gold)}
.checklist{left:27px;top:96px;width:340px}
.checklist__head{display:flex;align-items:baseline;border-bottom:.7px solid var(--gold);padding-bottom:2px}
.col-firm{width:39px;font-family:'Cormorant Garamond',serif;font-size:6px;padding-left:3px;color:#333}
.col-ours{width:37px;font-family:'Cormorant Garamond',serif;font-size:10px;color:#333}
.checklist__heading{font-family:'Cormorant Garamond',serif;font-weight:600;font-size:10.5px;color:var(--navy)}
.checklist__section+.checklist__section{margin-top:12px}
.checklist__row{display:flex;border-bottom:.6px solid var(--rule-light);padding:2.6px 0 2px;font-size:5.6px;line-height:7.8px;color:#333}
.checklist__row .tick{width:76px;padding-left:45px;color:var(--gold);font-size:7px;line-height:7.8px}
.checklist__row .item{flex:1}

/* commitment */
.commit-title{left:27px;top:225px;font-family:'Cormorant Garamond',serif;font-weight:700;font-size:15px;color:var(--navy)}
.commit-copy{left:27px;top:247px;width:330px;font-size:6.5px;line-height:10.3px;color:var(--ink-soft)}
.commit-copy p+p{margin-top:10.3px}
.checkup{left:27px;top:355px;width:336px;height:153px;background:var(--navy);color:#fff}
.checkup__title{left:17px;top:17px;font-family:'Cormorant Garamond',serif;font-weight:600;font-size:11px;line-height:14px;letter-spacing:.3px}
.checkup__photo{left:17px;top:55px;width:122px;height:67px;background:linear-gradient(135deg,#9aa4ad 0%,#d9dde0 45%,#5f6670 100%)}
.checkup__copy{left:162px;top:17px;width:162px;font-size:6.3px;line-height:9.6px}
.checkup__copy p+p{margin-top:9.6px}
</style>
</head>
<body>

<section class="page page--cover">
  <div class="page__panel"></div>
  <div class="abs brand-box">ALDER RIDGE<br>WEALTH MANAGEMENT</div>
  <h1 class="abs welcome-title">WELCOME<br>TO OUR TEAM!</h1>
  <div class="abs gold-rule"></div>
  <div class="abs cover-copy">
    <p><strong>Alder Ridge Wealth Management</strong> is a comprehensive financial services firm committed to helping our clients improve their long-term financial success. We offer a strong combination of experience and professional client services.</p>
    <p>We invite you to explore this brochure to compare our services to your current provider.</p>
  </div>
  <svg class="abs band" style="top:400px" width="392" height="108" viewBox="0 0 392 108">
    <defs><linearGradient id="coverBand" x1="0" y1="1" x2="1" y2="0"><stop offset="0" stop-color="#0a4e7a"/><stop offset="1" stop-color="#0b4266"/></linearGradient></defs>
    <polygon points="0,2 196,32 392,2 392,108 0,108" fill="url(#coverBand)"/>
    <polygon points="196,32 392,2 392,60" fill="var(--navy-deep)"/>
  </svg>
  <div class="abs contact">
    <div>418 Harbor Point Drive Suite 210</div>
    <div class="contact__grid">
      <div class="contact__col">
        <div><span class="contact__label">Phone.</span> (555) 310-4820</div>
        <div><span class="contact__label">Fax.</span> (555) 310-4821</div>
      </div>
      <div class="contact__col">
        <div><span class="contact__label">Email.</span> info@alderridge-wealth.com</div>
        <div><span class="contact__label">Web.</span> alderridge-wealth.com</div>
      </div>
    </div>
  </div>
</section>

<section class="page page--intro">
  <div class="page__panel"></div>
  <h2 class="abs intro-kicker">PERSONALIZED<span>GOLD CREST SERVICES</span></h2>
  <div class="abs intro-sub">THE NEW STANDARD IN WEALTH MANAGEMENT</div>
  <div class="abs intro-tagline">At Alder Ridge Wealth Management, clients come first!</div>
  <div class="abs intro-copy">
    <p>Our approach to delivering holistic financial services always starts and ends with you, our clients. We begin this process by listening to you and discussing your lifestyles, goals, wishes, dreams and family situations. Through a consultative process we then learn the details of your financial picture so we can construct and deliver a customized plan along with a properly allocated investment portfolio. Our experienced team of professionals fully evaluates your situation to prepare personal solutions that integrate investment planning, tax reduction planning, retirement income and distribution planning, as well as family wealth planning. We then schedule to meet with you on a regular basis to discuss and update your financial situation and make sure you are on track to reach your goals.</p>
    <p>We pride ourselves in our superior client services and regular client communications to keep you informed of economic news and appropriate tax law and estate planning rule updates.</p>
  </div>
  <svg class="abs band" style="top:278px" width="392" height="230" viewBox="0 0 392 230">
    <polygon points="0,0 197,23 392,0 392,230 0,230" fill="var(--navy)"/>
    <polygon points="197,23 392,0 392,30" fill="var(--navy-deep)"/>
  </svg>
  <div class="abs differ-title">Some of the ways we differ from other firms include:</div>
  <ul class="abs differ-list" style="left:41px;top:341px;width:146px">
    <li>Our strong menu of Gold Crest Services which include a comprehensive review of your: tax reduction strategies; estate plans; investment plans; retirement plans; and, protection plans.</li>
    <li>Our frequent and regularly scheduled meetings with clients to update your specific plans and discuss your personal situations.</li>
    <li>Our strong and consistent calendar of high quality newsletters, tax reports, and other reports and articles.</li>
  </ul>
  <ul class="abs differ-list" style="left:210px;top:341px;width:130px">
    <li>Our frequent schedule of client educational and appreciation events.</li>
    <li>Our personal service that features our best and most current ideas, suggestions and solutions.</li>
  </ul>
</section>

<section class="page page--compare">
  <div class="page__panel"></div>
  <div class="abs badge"><div class="badge__square"></div>GOLD CREST<br>SERVICES</div>
  <h2 class="abs compare-title">COMPARE OUR LIST OF <span>GOLD CREST<br>SERVICES</span> TO THE SERVICES YOU<br>RECEIVE TODAY.</h2>
  <div class="abs checklist">
    <div class="checklist__section">
      <div class="checklist__head"><span class="col-firm">Your Firm</span><span class="col-ours">Alder</span><span class="checklist__heading">Financial Planning</span></div>
      <div class="checklist__row"><span class="tick">✓</span><span class="item">Clients will receive a full comprehensive financial plan</span></div>
      <div class="checklist__row"><span class="tick">✓</span><span class="item">Discussion and analysis of your financial needs now and in the future</span></div>
      <div class="checklist__row"><span class="tick">✓</span><span class="item">Analysis of all current and future economic resources</span></div>
      <div class="checklist__row"><span class="tick">✓</span><span class="item">Continual development and implementation of recommendations to fund your financial needs and help maintain a comfortable standard of living</span></div>
    </div>
    <div class="checklist__section">
      <div class="checklist__head"><span class="col-firm"></span><span class="col-ours"></span><span class="checklist__heading">Investment Oversight Service</span></div>
      <div class="checklist__row"><span class="tick">✓</span><span class="item">Reviewing your investments and designing a personalized portfolio appropriate to your needs</span></div>
      <div class="checklist__row"><span class="tick">✓</span><span class="item">Year-long, continual monitoring of your investments</span></div>
      <div class="checklist__row"><span class="tick">✓</span><span class="item">Regular review of your investment accounts to rebalance and manage to your personalized investment strategy</span></div>
      <div class="checklist__row"><span class="tick">✓</span><span class="item">Monthly and/or quarterly statements</span></div>
      <div class="checklist__row"><span class="tick">✓</span><span class="item">Independent Advice</span></div>
      <div class="checklist__row"><span class="tick">✓</span><span class="item">Recommendations regarding positioning of investments within your employer provided retirement plans such as 401(k)s</span></div>
    </div>
    <div class="checklist__section">
      <div class="checklist__head"><span class="col-firm"></span><span class="col-ours"></span><span class="checklist__heading">Tax Reduction Planning</span></div>
      <div class="checklist__row"><span class="tick">✓</span><span class="item">Complimentary consultation with your tax preparer</span></div>
      <div class="checklist__row"><span class="tick">✓</span><span class="item">Recommendations of tax solutions including tax advantaged investments</span></div>
      <div class="checklist__row"><span class="tick">✓</span><span class="item">Special reports on how to help reduce your taxes and other important topics</span></div>
      <div class="checklist__row"><span class="tick">✓</span><span class="item">Staying up-to-date on new tax laws that can affect your situation</span></div>
    </div>
    <div class="checklist__section">
      <div class="checklist__head"><span class="col-firm"></span><span class="col-ours"></span><span class="checklist__heading">Family Wealth Planning</span></div>
      <div class="checklist__row"><span class="tick">✓</span><span class="item">Analysis of your current estate plan and concerns</span></div>
      <div class="checklist__row"><span class="tick">✓</span><span class="item">Complimentary consultation with your attorney</span></div>
      <div class="checklist__row"><span class="tick">✓</span><span class="item">Assistance in transferring assets to your Living Trust or other trusts</span></div>
      <div class="checklist__row"><span class="tick">✓</span><span class="item">Analysis of the beneficiaries of your IRA and how to establish an Inherited IRA</span></div>
      <div class="checklist__row"><span class="tick">✓</span><span class="item">Providing guidance with the appropriate and necessary steps in the event of the death of a loved one</span></div>
    </div>
  </div>
</section>

<section class="page page--commitment">
  <div class="page__panel"></div>
  <div class="abs badge"><div class="badge__square"></div>GOLD CREST<br>SERVICES</div>
  <h2 class="abs compare-title">COMPARE OUR LIST OF <span>GOLD CREST<br>SERVICES</span> TO THE SERVICES YOU<br>RECEIVE TODAY.</h2>
  <div class="abs checklist">
    <div class="checklist__section">
      <div class="checklist__head"><span class="col-firm">Your Firm</span><span class="col-ours">Alder</span><span class="checklist__heading">Client Services &amp; Communications</span></div>
      <div class="checklist__row"><span class="tick">✓</span><span class="item">Access to our customized online wealth management portal</span></div>
      <div class="checklist__row"><span class="tick">✓</span><span class="item">Quarterly “market watch” letters detailing our firms research, analysis, and view of the current state of the investment markets</span></div>
      <div class="checklist__row"><span class="tick">✓</span><span class="item">Economic and educational seminars held throughout the year (guests welcome)</span></div>
      <div class="checklist__row"><span class="tick">✓</span><span class="item">Special Gold Crest Service Events, including client appreciation events (where you may bring up to 2 guests)</span></div>
      <div class="checklist__row"><span class="tick">✓</span><span class="item">Annual meetings to review and evaluate your investment performance, portfolio allocation, and update your financial plan.</span></div>
    </div>
  </div>
  <h3 class="abs commit-title">Our Commitment to You...</h3>
  <div class="abs commit-copy">
    <p>Alder Ridge Wealth Management was founded with the goal of assisting clients in every aspect of their financial lives. We offer all clients personal, customized service. For each of our clients, we strive to help create financial stability and confidence to provide financial independence.</p>
    <p>Our staff consists of experienced professionals with a "hands on" approach to financial guidance. Our team members are knowledgeable and truly care about helping our clients achieve their goals. We do everything in our power to keep our clients focused on where they want to go, advise them on how to get there, and continually remind them of the importance of maintaining a disciplined approach to realizing their financial goals and dreams.</p>
  </div>
  <div class="abs checkup">
    <h3 class="abs checkup__title">COMPLIMENTARY<br>FINANCIAL CHECK-UP</h3>
    <div class="abs checkup__photo" role="img" aria-label="Photo of an advisor meeting a client at a desk"></div>
    <div class="abs checkup__copy">
      <p>Alder Ridge Wealth Management would like to offer you a complimentary financial check-up. We pride ourselves on providing prompt, personal and highly professional services.</p>
      <p>We want to offer you a complimentary, one-hour, private consultation with one of our professionals at absolutely no cost or obligation to you.</p>
      <p>To schedule your complimentary financial check-up, please call <strong>Eleanor at (555) 310-4820</strong></p>
    </div>
  </div>
</section>

</body>
</html>
```